Corvane Networks web design

Corvane is an Internet Service Provider bringing high-speed service to homes and businesses. Our principal market target is rural areas of West Michigan, but we intend to expand rapidly. We need a website to market our services, facilitate online ordering, customer support and communicate with our customers.

I will upload a draft outline of the content we hope to include in the website.

We compete directly with Halberd Communications, Lumetra, Dravix and Kelwick communications to bring Internet service to homes and businesses in our coverage area.

Our primary values include:

1. Unlike our competitors, we do not require long term contractors or service bundles; There are no termination fees, for example. All services are sold on a recurring 1-month agreement term.
2. Unlike other wireless (mobile) providers, we do not limit downloads or uploads with bit/byte buckets
3. We provide service to areas ignored by the larger carriers - Rural areas in Michigan that lack options for broadband are prime targets for Corvane to cover.
4. Unlike other wireless ISP's, we utilize licensed FCC spectrum. We do not use unlicensed/free frequencies, providing us an advantage for reliability and stability.
Updates

So many wonderful designs, thank you very much for all your hard work. We are evaluating all our favorite designs and plan to make a selection in the next 2 days. I will be in touch with you to request revisions if necessary or further refinements.  Thank you again for your efforts on this project.

Target Market(s)

Our target market is home Internet users. however, that does not mean that our users are "high tech" oriented - they are just normal mom's and pop's who buy Internet for home use. The site should be easy to navigate and communicate our message of speed, value, reliability and facilitate simple product ordering.

Industry/Entity Type

Internet

Requirements
Must have
• Our phone number should be prominently displayed 1-844-7NU-LINK
• Our logo is uploaded in the attachments.
• Design for desktop and mobile devices.
Nice to have
• The most modern of web design trends. Such as a design that facilitates parallax scrolling effects rather than lots of individual pages.
• Stock artwork communicating our values of speed and reliability.

```html
<!DOCTYPE html>
<html lang="en">
<head>
<meta charset="utf-8">
<title>Corvane Networks</title>
<link href="https://fonts.googleapis.com/css2?family=Montserrat:wght@400;600;700&family=Open+Sans:wght@400;600&display=swap" rel="stylesheet">
<style>
:root{
  --orange:#f07d1a;
  --dark:#3a3d41;
  --ink:#333;
  --muted:#888;
  --link:#2aa3c9;
  --footer-text:#c9ccd0;
  --hero-a:#6f6558;
  --hero-b:#9b8f80;
  --hero-c:#d8d4ce;
}
*{margin:0;padding:0;box-sizing:border-box}
html,body{width:913px;height:1200px;overflow:hidden;background:#fff}
body{position:relative;font-family:"Open Sans",sans-serif;color:var(--ink)}
.abs{position:absolute}
.header{left:0;top:0;width:913px;height:82px;background:#fff}
.brand{left:98px;top:26px;display:flex;align-items:center;gap:8px;font-family:"Montserrat",sans-serif;font-weight:700;font-size:22px;color:var(--orange);letter-spacing:1px}
.brand-mark{width:12px;height:12px;border-radius:50%;background:var(--orange)}
.nav{top:36px;font-family:"Montserrat",sans-serif;font-size:11.5px;color:#555}
.phone-btn{left:679px;top:24px;width:142px;height:31px;background:var(--dark);color:#fff;font-family:"Montserrat",sans-serif;font-weight:700;font-size:13px;display:flex;align-items:center;justify-content:center}
.hero{left:0;top:82px;width:913px;height:511px;overflow:hidden;background:linear-gradient(90deg,var(--hero-a) 0%,var(--hero-b) 48%,var(--hero-c) 100%)}
.hero-person{left:470px;top:0;width:443px;height:511px;background:linear-gradient(90deg,rgba(60,45,36,0) 0%,rgba(60,45,36,.55) 40%,rgba(50,40,34,.7) 70%,rgba(60,50,44,.2) 100%)}
.hero-title{left:94px;top:172px;width:420px;font-family:"Montserrat",sans-serif;font-weight:600;font-size:31px;line-height:37px;color:#fff}
.hero-lead{left:97px;top:254px;width:370px;font-family:"Montserrat",sans-serif;font-size:12.6px;line-height:19px;color:#fff}
.hero-list{left:97px;top:324px;list-style:none;font-family:"Montserrat",sans-serif;font-size:13px;color:#f2f0ec}
.hero-list li{height:26px;display:flex;align-items:center;gap:7px}
.hero-list svg{width:12px;height:12px}
.section-title{top:623px;font-family:"Montserrat",sans-serif;font-weight:700;font-size:14px;color:#3a3a3a}
.post-icon{width:38px;height:38px;display:flex;align-items:center;justify-content:center}
.post-date{width:38px;text-align:center;font-style:italic;color:#444}
.post-date b{display:block;font-weight:400;font-size:18px;line-height:18px}
.post-date span{font-size:8px}
.post{left:160px;width:170px}
.post h4{font-weight:400;font-size:10.2px;line-height:13px;color:#222}
.post p{margin-top:9px;font-size:9.8px;line-height:14px;color:var(--muted)}
.post a{display:block;margin-top:6px;font-size:11px;color:var(--orange);text-decoration:none}
.rule{height:4px;background:repeating-linear-gradient(45deg,#ddd 0 1px,#fff 1px 3px)}
.tweet-dot{left:359px;width:26px;height:26px;border-radius:50%;background:var(--link)}
.tweet{left:401px;width:170px;font-size:9.8px;line-height:15px;color:#666}
.tweet .handle{color:var(--link)}
.tweet .ago{color:#bbb}
.staff-photo{left:594px;width:82px;height:67px;border:1px solid #ddd;background:linear-gradient(135deg,#e9edf1,#b9c3cc)}
.staff{left:688px;width:140px}
.staff h5{font-family:"Montserrat",sans-serif;font-weight:600;font-size:11.5px;color:#333}
.staff p{margin-top:6px;font-size:8.8px;line-height:14px;color:var(--muted)}
.footer{left:0;top:935px;width:913px;height:265px;background:var(--dark)}
.f-col{top:978px;font-family:"Montserrat",sans-serif;color:var(--footer-text);font-size:9.3px;line-height:16.8px;text-transform:uppercase}
.f-col h6{font-weight:400;font-size:10.8px;color:#fff;margin-bottom:4px}
.f-contact{font-size:11.5px;text-transform:none}
.f-rule{left:100px;top:1142px;width:722px;height:1px;background:#4a4d52}
.copyright{left:112px;top:1164px;font-family:"Montserrat",sans-serif;font-size:9.3px;color:#c0c3c7}
</style>
</head>
<body>
<header class="header abs">
  <div class="brand abs"><span class="brand-mark"></span>CORVANE</div>
  <span class="nav abs" style="left:298px">Home</span>
  <span class="nav abs" style="left:353px">Services</span>
  <span class="nav abs" style="left:424px">Wireless</span>
  <span class="nav abs" style="left:494px">Coverage</span>
  <span class="nav abs" style="left:572px">Contact us</span>
  <div class="phone-btn abs">1-844-7NU-LINK</div>
</header>

<section class="hero abs" role="img" aria-label="Office photo of a smiling businesswoman holding a tablet">
  <div class="hero-person abs"></div>
</section>
<h1 class="hero-title abs">West Michigan’s Best Internet Service</h1>
<p class="hero-lead abs">Corvane Networks is a Michigan-based company providing high-speed Internet services to West Michigan homes and businesses.</p>
<ul class="hero-list abs">
  <li><svg viewBox="0 0 12 12"><path d="M1 6.5l3 3 7-8" fill="none" stroke="#fff" stroke-width="1.6"/></svg>100% Satisfaction Guaranteed.</li>
  <li><svg viewBox="0 0 12 12"><path d="M1 6.5l3 3 7-8" fill="none" stroke="#fff" stroke-width="1.6"/></svg>Honest Pricing, No Hidden Fees</li>
  <li><svg viewBox="0 0 12 12"><path d="M1 6.5l3 3 7-8" fill="none" stroke="#fff" stroke-width="1.6"/></svg>No Long Term Contracts.</li>
  <li><svg viewBox="0 0 12 12"><path d="M1 6.5l3 3 7-8" fill="none" stroke="#fff" stroke-width="1.6"/></svg>No Phone Line or Cable TV required.</li>
  <li><svg viewBox="0 0 12 12"><path d="M1 6.5l3 3 7-8" fill="none" stroke="#fff" stroke-width="1.6"/></svg>Fast, Superior Performance for your home and business.</li>
  <li><svg viewBox="0 0 12 12"><path d="M1 6.5l3 3 7-8" fill="none" stroke="#fff" stroke-width="1.6"/></svg>Interference-Free FCC Licensed 4G Coverage.</li>
</ul>

<h2 class="section-title abs" style="left:97px">COMPANY’S BLOG</h2>
<h2 class="section-title abs" style="left:349px">LATEST TWEETS</h2>
<h2 class="section-title abs" style="left:590px">OUR STAFF</h2>

<div class="post-icon abs" style="left:99px;top:663px;background:#e0561a">
  <svg width="18" height="18" viewBox="0 0 18 18"><path d="M3 13V9a6 6 0 0 1 12 0v4" fill="none" stroke="#fff" stroke-width="2"/><rect x="2" y="11" width="3" height="5" fill="#fff"/><rect x="13" y="11" width="3" height="5" fill="#fff"/></svg>
</div>
<div class="post-date abs" style="left:99px;top:708px"><b>31</b><span>01,13</span></div>
<div class="post abs" style="top:668px">
  <h4>Contrary to popula belieflorem the Ipsum is simply</h4>
  <p>Lorem Ipsum is dummy text the printing and typesetting instry. Ipsum has been.Lorem Ipsis sly</p>
  <a href="#">View More</a>
</div>
<div class="rule abs" style="left:99px;top:781px;width:229px"></div>
<div class="post-icon abs" style="left:99px;top:799px;background:#6aa9cf">
  <svg width="18" height="16" viewBox="0 0 18 16"><rect x="1" y="1" width="16" height="14" fill="none" stroke="#fff" stroke-width="1.5"/><path d="M3 13l4-5 3 3 2-2 3 4z" fill="#fff"/><circle cx="12" cy="5" r="1.5" fill="#fff"/></svg>
</div>
<div class="post-date abs" style="left:99px;top:844px"><b>31</b><span>01,13</span></div>
<div class="post abs" style="top:804px">
  <h4>Contrary to popula belieflorem the Ipsum is simply</h4>
  <p>Lorem Ipsum is dummy text the printing and typesetting instry. Ipsum has been.Lorem Ipsis sly</p>
  <a href="#">View More</a>
</div>

<div class="tweet-dot abs" style="top:663px"></div>
<p class="tweet abs" style="top:659px"><span class="handle">@mira_holten</span> Lorem Ipsum is the dummy text the printing typeset- ting instry Ipsum is has been.Lorem<br><span class="ago">3 days ago</span></p>
<div class="rule abs" style="left:348px;top:729px;width:221px"></div>
<div class="tweet-dot abs" style="top:747px"></div>
<p class="tweet abs" style="top:743px"><span class="handle">@mira_holten</span> Lorem Ipsum is the dummy text the printing typeset- ting instry Ipsum is has been.Lorem<br><span class="ago">3 days ago</span></p>
<div class="rule abs" style="left:348px;top:814px;width:221px"></div>
<div class="tweet-dot abs" style="top:830px"></div>
<p class="tweet abs" style="top:826px"><span class="handle">@mira_holten</span> Lorem Ipsum is the dummy text the printing typeset- ting instry Ipsum is has been.Lorem<br><span class="ago">3 days ago</span></p>

<div class="staff-photo abs" style="top:663px" role="img" aria-label="Staff portrait"></div>
<div class="staff abs" style="top:665px"><h5>LOREM IPSUM</h5><p>Lorem Ipsum Dolor sit amet and typesetting industry and ipsum and ending etc</p></div>
<div class="staff-photo abs" style="top:741px" role="img" aria-label="Staff portrait"></div>
<div class="staff abs" style="top:743px"><h5>LOREM IPSUM</h5><p>Lorem Ipsum Dolor sit amet and typesetting industry and ipsum and ending etc</p></div>
<div class="staff-photo abs" style="top:819px" role="img" aria-label="Staff portrait"></div>
<div class="staff abs" style="top:822px"><h5>LOREM IPSUM</h5><p>Lorem Ipsum Dolor sit amet and typesetting industry and ipsum and ending etc</p></div>

<footer class="footer abs"></footer>
<div class="f-col abs" style="left:104px">
  <h6>EXPLORE</h6>
  Service Plans<br>Coverage Map<br>Who is Corvane<br>Company Blog<br>Cusomer Support<br>Account Management
</div>
<div class="f-col abs" style="left:277px">
  <h6>SUPPORT STAFF HOURS</h6>
  Weekdays 7 AM to 10PM<br>Weekends 8 AM to 5PM<br>Holiday Scheduling Varies
</div>
<div class="f-col abs" style="left:474px">
  <h6>LATEST NEWS</h6>
  Lorem Ipsum Dolor Sit<br>Aemet Lorem Ipsum Dolor<br>Sit Aemet
</div>
<div class="f-col abs" style="left:677px;top:977px">
  <h6>LOCATION</h6>
  Corvane Networks, LLC<br>2180 Alder Ridge Road<br>Grand Haven, MI 49417
  <h6 style="margin-top:20px">CONTACT</h6>
  <span class="f-contact">616-555-0148</span>
</div>
<div class="f-rule abs"></div>
<p class="copyright abs">©COPYRIGHT 2014. ALL RIGHTS RESERVED</p>
</body>
</html>
```